Business Card for Marco Thieblin Analytics and Marco Thieblin Photography

I want a double sided business card: on one side it should be about "Marco Thieblin Photography" and on the other side about "Marco Thieblin Analytics". You find the logos for these two projects in the attachments. The design of the business card should blend well with the colours and fonts used in the logos and should be quite simple, yet look professional and modern.

In addition to my name, there should be content for a telephone number, e-mail address and website. There should be little icons (for telephone, email and web) before these fields. I do not want a postal mail address field.
Lastly you should indicate that people can contact me in the following languages: Lëtzebuergesch, Deutsch, Français, English, Castellano, Ido
This should be very unobtrusive: either in a small muted font or with little icons (preferably without using flags as flags represent nations, not languages - one possibility would be by using the 2 letter ISO codes).

The design should be delivered in Adobe Illustrator format or something similar that I can edit easily, as it's possible that I will change my e-mail address and domain soon.

I hope this was detailed enough but still leaves you some freedom for designing something nice.

Thank you!
Marco

Industry/Entity Type

Business

Contact Information for Business Card

e-mail address: mtb_@orvenmail.example
website: www.marcothieblin.example (for Marco Thieblin Photography)
website: kelvodata.example/mtb (for Marco Thieblin Analytics - this address is likely to change)
phone: +352 691 987 654 (not my real number - I prefer not to publish it on the web)

Requirements
Nice to have
• A speech bubble followed by the 2-letter language codes (lb, de, fr, en, es, io) or even speech bubble icons for every language would be nice and eliminates the need to put text like 'you can contact me in the following languages'.

```html
<!DOCTYPE html>
<html lang="en">
<head>
<meta charset="utf-8">
<title>Marco Thieblin – Business Cards</title>
<link href="https://fonts.googleapis.com/css2?family=Lato:wght@400;700&family=Alex+Brush&display=swap" rel="stylesheet">
<style>
  :root {
    --canvas: #d9d9d9;
    --card-dark: #1f1e1e;
    --card-light: #ffffff;
    --orange: #f0801f;
    --green: #2aa84a;
    --blue: #1a8fd1;
    --ink: #2b2b2b;
    --muted-light: #c9c9c9;
    --divider: #9a9a9a;
  }
  * { margin: 0; padding: 0; box-sizing: border-box; }
  html, body { width: 1200px; height: 1200px; overflow: hidden; }
  body {
    background: var(--canvas);
    font-family: "Lato", sans-serif;
    position: relative;
  }
  .card {
    position: absolute;
    left: 180px;
    width: 840px;
    height: 543px;
    border-radius: 6px;
    box-shadow: 0 6px 18px rgba(0,0,0,.18);
    overflow: hidden;
  }

  /* Photography side */
  .card--photography { top: 38px; background: var(--card-dark); color: var(--muted-light); }
  .photo-brand {
    position: absolute; top: 150px; left: 0; right: 0;
    text-align: center;
    display: flex; align-items: center; justify-content: center; gap: 16px;
  }
  .brand-dot { width: 22px; height: 22px; border-radius: 50%; background: var(--orange); }
  .photo-brand__name { font-size: 40px; font-weight: 400; color: var(--orange); letter-spacing: .5px; }
  .photo-web {
    position: absolute; top: 215px; left: 0; right: 0; text-align: center;
    font-size: 22px; color: var(--orange); letter-spacing: 1px;
  }
  .languages-intro {
    position: absolute; top: 300px; left: 0; right: 0; text-align: center;
    font-size: 24px; color: var(--muted-light);
  }
  .languages-rule {
    position: absolute; top: 345px; left: 170px; right: 170px;
    height: 1px; background: #4a4a4a;
  }
  .languages {
    position: absolute; top: 370px; left: 0; right: 0;
    display: flex; justify-content: center; gap: 30px;
    list-style: none;
  }
  .language { display: flex; align-items: center; gap: 8px; font-size: 24px; color: var(--muted-light); }
  .language__mark { width: 30px; height: 20px; border-radius: 2px; }
  .mark-lb { background: #3d7fd0; }
  .mark-de { background: linear-gradient(#111 33%, #d4202a 33% 66%, #f5c400 66%); }
  .mark-fr { background: linear-gradient(90deg, #2a4fa3 33%, #fff 33% 66%, #d4202a 66%); }
  .mark-en { background: #2a3d8f; }
  .mark-es { background: linear-gradient(#c8202a 25%, #f5c400 25% 75%, #c8202a 75%); }
  .mark-io { background: #4a90d9; }

  /* Analytics side */
  .card--analytics { top: 619px; background: var(--card-light); color: var(--ink); }
  .analytics-brand {
    position: absolute; top: 210px; left: 50px; width: 330px;
    display: flex; align-items: center; gap: 12px;
  }
  .analytics-brand .brand-dot { background: var(--green); width: 18px; height: 18px; flex: none; }
  .analytics-brand__name { font-size: 30px; color: var(--orange); line-height: 1.15; }
  .card-divider {
    position: absolute; left: 410px; top: 150px; width: 1px; height: 240px;
    background: var(--divider);
  }
  .contact-name {
    position: absolute; left: 450px; top: 135px;
    font-family: "Alex Brush", cursive; font-size: 62px; color: var(--orange);
  }
  .contact-list {
    position: absolute; left: 452px; top: 250px; list-style: none;
  }
  .contact-item {
    display: flex; align-items: center; gap: 14px;
    font-size: 27px; color: var(--ink); margin-bottom: 16px;
  }
  .contact-item svg { width: 26px; height: 26px; flex: none; }
</style>
</head>
<body>

<section class="card card--photography" aria-label="Photography side">
  <div class="photo-brand">
    <span class="brand-dot"></span>
    <span class="photo-brand__name">Marco Thieblin Photography</span>
  </div>
  <p class="photo-web">www.marcothieblin.example</p>
  <p class="languages-intro">You Can Contact Me In The Following Languages</p>
  <div class="languages-rule"></div>
  <ul class="languages">
    <li class="language"><span class="language__mark mark-lb" role="img" aria-label="Language marker"></span>LB</li>
    <li class="language"><span class="language__mark mark-de" role="img" aria-label="Language marker"></span>DE</li>
    <li class="language"><span class="language__mark mark-fr" role="img" aria-label="Language marker"></span>FR</li>
    <li class="language"><span class="language__mark mark-en" role="img" aria-label="Language marker"></span>EN</li>
    <li class="language"><span class="language__mark mark-es" role="img" aria-label="Language marker"></span>ES</li>
    <li class="language"><span class="language__mark mark-io" role="img" aria-label="Language marker"></span>IO</li>
  </ul>
</section>

<section class="card card--analytics" aria-label="Analytics side">
  <div class="analytics-brand">
    <span class="brand-dot"></span>
    <span class="analytics-brand__name">Marco Thieblin Analytics</span>
  </div>
  <div class="card-divider"></div>
  <p class="contact-name">Marco Thieblin</p>
  <ul class="contact-list">
    <li class="contact-item">
      <svg viewBox="0 0 24 24" aria-hidden="true"><path fill="var(--orange)" d="M6.6 10.8a15.1 15.1 0 0 0 6.6 6.6l2.2-2.2a1 1 0 0 1 1-.25 11.4 11.4 0 0 0 3.6.57 1 1 0 0 1 1 1V20a1 1 0 0 1-1 1A17 17 0 0 1 3 4a1 1 0 0 1 1-1h3.5a1 1 0 0 1 1 1c0 1.25.2 2.45.57 3.57a1 1 0 0 1-.25 1z"/></svg>
      +352 691 987 654
    </li>
    <li class="contact-item">
      <svg viewBox="0 0 24 24" aria-hidden="true"><rect x="2" y="5" width="20" height="14" rx="1.5" fill="var(--orange)"/><path d="M3 6l9 7 9-7" fill="none" stroke="#fff" stroke-width="1.6"/></svg>
      mtb_@orvenmail.example
    </li>
    <li class="contact-item">
      <svg viewBox="0 0 24 24" aria-hidden="true"><g fill="none" stroke="var(--orange)" stroke-width="2"><circle cx="12" cy="12" r="9"/><ellipse cx="12" cy="12" rx="4" ry="9"/><path d="M3 12h18"/></g></svg>
      kelvodata.example/mtb
    </li>
  </ul>
</section>

</body>
</html>
```